Business Card Design Project

The overall design must be suitable alongside our company logo which is attached

There must be space for the agent to write their name & telephone number

Card must contain the words:

Brightwell Carpet Cleaning

Agent:
Tel:

Target Market(s)

qweqwe

Industry/Entity Type

Business

```html
<!DOCTYPE html>
<html lang="en">
<head>
<meta charset="utf-8">
<title>Brightwell Carpet Cleaning – Business Card</title>
<link rel="stylesheet" href="https://fonts.googleapis.com/css2?family=Open+Sans:wght@400;600&display=swap">
<style>
  :root {
    --page-bg: #eeeeee;
    --card-white: #ffffff;
    --card-dark: #2a211c;
    --gold: #d6a042;
    --gold-deep: #b98228;
    --ink: #231a15;
    --field-white: #ffffff;
  }
  * { box-sizing: border-box; margin: 0; padding: 0; }
  html, body {
    width: 1200px;
    height: 900px;
    overflow: hidden;
    background: var(--page-bg);
    font-family: "Open Sans", Arial, sans-serif;
  }
  .business-card {
    position: absolute;
    left: 100px;
    top: 160px;
    width: 1000px;
    height: 580px;
    border-radius: 48px;
    overflow: hidden;
    background: var(--card-white);
    box-shadow: 0 18px 40px rgba(0, 0, 0, 0.18);
  }
  .card-shapes {
    position: absolute;
    inset: 0;
    width: 100%;
    height: 100%;
  }
  .brand-mark {
    position: absolute;
    left: 60px;
    top: 240px;
    display: flex;
    align-items: center;
    gap: 18px;
  }
  .brand-mark__dot {
    width: 64px;
    height: 64px;
    border-radius: 50%;
    background: var(--gold);
    flex: none;
  }
  .brand-mark__name {
    font-size: 56px;
    font-weight: 600;
    color: var(--ink);
    line-height: 1;
  }
  .card-details {
    position: absolute;
    left: 700px;
    top: 0;
    width: 260px;
    height: 100%;
    display: flex;
    flex-direction: column;
    align-items: center;
    text-align: center;
  }
  .card-details__company {
    margin-top: 60px;
    font-size: 52px;
    font-weight: 600;
    color: var(--gold);
    line-height: 1.1;
  }
  .card-details__service {
    font-size: 36px;
    font-weight: 400;
    color: #ffffff;
    line-height: 1.2;
    white-space: nowrap;
  }
  .write-in {
    width: 270px;
    margin-top: 40px;
  }
  .write-in + .write-in { margin-top: 26px; }
  .write-in__label {
    display: block;
    font-size: 26px;
    color: var(--gold);
    line-height: 1.3;
  }
  .write-in__field {
    display: block;
    height: 54px;
    background: var(--field-white);
    border: 4px solid var(--gold);
  }
</style>
</head>
<body>
  <div class="business-card">
    <svg class="card-shapes" viewBox="0 0 1000 580" preserveAspectRatio="none" aria-hidden="false">
      <defs>
        <linearGradient id="gold-sweep" x1="0" y1="0" x2="0" y2="1">
          <stop offset="0" stop-color="#e2b55a"/>
          <stop offset="1" stop-color="#b98228"/>
        </linearGradient>
      </defs>
      <path class="gold-swoosh" fill="url(#gold-sweep)"
            d="M470 0 H640 C690 170 690 390 650 580 H630 C650 380 610 160 470 0 Z"/>
      <path class="dark-panel" fill="var(--card-dark)" role="img"
            aria-label="Dark brown panel with a subtle damask pattern"
            d="M605 0 H1000 V580 H650 C685 390 675 170 605 0 Z"/>
    </svg>

    <div class="brand-mark">
      <span class="brand-mark__dot"></span>
      <span class="brand-mark__name">Brightwell</span>
    </div>

    <div class="card-details">
      <p class="card-details__company">Brightwell</p>
      <p class="card-details__service">Carpet Cleaning</p>
      <div class="write-in">
        <span class="write-in__label">Agent</span>
        <span class="write-in__field"></span>
      </div>
      <div class="write-in">
        <span class="write-in__label">Tel</span>
        <span class="write-in__field"></span>
      </div>
    </div>
  </div>
</body>
</html>
```